Website design and Setup for Real Estate Firm and Going Live

We are a commercial real estate investment firm and are looking for a 6 page website which is informational only. Some text and graphics on each page. We would want the designer to code and launch the website. This website needs to be corporate looking as well as innovative. We are setting up the website on hostivo.

The first page will be a home page with generic commercial real estate look with a link to the following 5 pages on page 1. So page one (the Home Page should have a commercial real estate look with the text linking to the following pages. Page 2 "About Us" with 3 paragraphs describing our firm. Page 3 "Our Platform" with another few paragraphs on due diligence, acquisitions, financing, and management.

Page 4 is "Our Team" highlighting several manager profiles. Page 5 is our "investment Portfolio portal" which will be password protected so not a lot of text, only general graphics and anyone viewing the site casually won't get into the backend, Page 6 is the contact us page. All of the content will be uploaded shortly.

The project includes setting up hyperlinks in the website as well rotating images etc and a final complete live online product. We do not expect to pay for any stock images.

Target Market(s)

Investors, Real Estate Professionals, Brokerages

Industry/Entity Type

Real Estate

Coding

Coded - Design and coding required

Number of Pages Required

5+ page

Requirements
Must have
• Corporate cutting edge design, suitable for a financial corporation.

```html
<!DOCTYPE html>
<html lang="en">
<head>
<meta charset="utf-8">
<title>Northvale Equities — Real Estate Investment Firm</title>
<link rel="stylesheet" href="https://fonts.googleapis.com/css2?family=Playfair+Display:wght@400;500&family=Montserrat:wght@400;500;600;700&display=swap">
<style>
:root{
  --ink:#2b2f36;
  --dark:#363b44;
  --slate:#3c4149;
  --grey:#8e9196;
  --light-grey:#a6a8ab;
  --pale:#f1f1f1;
  --white:#ffffff;
  --serif:'Playfair Display', Georgia, serif;
  --sans:'Montserrat', Arial, sans-serif;
}
*{box-sizing:border-box;margin:0;padding:0}
html,body{width:1200px;height:3863px;overflow:hidden;background:var(--white);font-family:var(--sans);color:var(--ink)}
.page{position:relative;width:1200px;height:3863px;overflow:hidden}

/* header */
.site-header{position:absolute;left:0;top:0;width:1200px;height:130px;background:var(--white);z-index:3}
.brand{position:absolute;left:92px;top:22px;width:215px;text-align:center}
.brand-mark{display:block;width:46px;height:46px;margin:0 auto 8px;background:var(--light-grey)}
.brand-name{font-family:var(--serif);font-size:21px;color:var(--grey);letter-spacing:.5px;white-space:nowrap}
.brand-tag{font-size:7px;letter-spacing:4px;color:var(--light-grey);margin-top:2px}
.call-btn{position:absolute;left:826px;top:0;width:257px;height:45px;background:var(--light-grey);color:var(--white);font-size:13px;font-weight:600;letter-spacing:1px;display:flex;align-items:center;justify-content:center;gap:8px}
.main-nav{position:absolute;top:82px;left:343px;display:flex}
.main-nav a{font-size:11.5px;letter-spacing:.8px;color:var(--grey);text-decoration:none;font-weight:500;margin-right:36px;position:relative}
.main-nav a.active{color:var(--ink);font-weight:600}
.main-nav a.active::after{content:"";position:absolute;left:-3px;right:-3px;top:42px;height:3px;background:var(--light-grey)}

/* hero */
.hero{position:absolute;left:0;top:130px;width:1200px;height:653px;background:linear-gradient(180deg,#1a5ec4 0%,#3a86de 35%,#9ab9dc 55%,#e8eef6 72%,#b5c8e2 100%)}
.hero-title{position:absolute;top:142px;width:100%;text-align:center;font-family:var(--serif);font-size:70px;font-weight:400;color:var(--white);letter-spacing:1px}
.hero-sub{position:absolute;top:228px;width:100%;text-align:center;font-size:26px;color:var(--white);letter-spacing:5px}
.hero-btn{position:absolute;top:282px;width:179px;height:44px;display:flex;align-items:center;justify-content:center;color:var(--white);font-size:12px;letter-spacing:1.5px;font-weight:500}
.hero-btn.fill{left:407px;background:rgba(160,163,167,.9)}
.hero-btn.ghost{left:596px;border:2px solid var(--white)}

/* shared */
.eyebrow{font-size:20px;letter-spacing:3px;color:var(--ink);line-height:24px}
.section-title{font-family:var(--serif);font-size:44px;color:var(--ink);font-weight:400;line-height:1.1}
.body-text{font-size:16px;line-height:28px;color:#55585e}
.outline-btn{position:absolute;width:181px;height:48px;border:2px solid var(--dark);display:flex;align-items:center;justify-content:center;font-size:12.5px;font-weight:600;letter-spacing:2px;color:var(--ink)}

/* about */
.about{position:absolute;left:0;top:783px;width:1200px;height:602px}
.about-bg-photo{position:absolute;left:0;top:0;width:394px;height:602px;background:linear-gradient(160deg,#c8cbcf,#9fa3a8 60%,#b6b9bd)}
.about-frame{position:absolute;left:115px;top:53px;width:253px;height:245px;border-top:2px solid #eceded;border-left:2px solid #eceded}
.about-photo{position:absolute;left:129px;top:67px;width:421px;height:453px;background:linear-gradient(135deg,#5a5e63 0%,#c9cbce 40%,#f4f5f6 55%,#6d7176 80%,#45494e 100%)}
.about-dots{position:absolute;left:445px;top:412px;width:128px;height:128px;background-image:radial-gradient(#3b3f45 1px,transparent 1.4px);background-size:5px 5px;clip-path:polygon(75% 0,100% 0,100% 100%,0 100%,0 85%,75% 85%)}
.about .eyebrow{position:absolute;left:616px;top:136px}
.about .section-title{position:absolute;left:616px;top:160px}
.about .rule{position:absolute;left:618px;top:216px;width:40px;height:2px;background:var(--ink)}
.about .body-text{position:absolute;left:616px;top:251px;width:462px}
.about .outline-btn{left:619px;top:397px}

/* approach */
.approach{position:absolute;left:0;top:1385px;width:1200px;height:628px;background:var(--pale)}
.approach .section-title{position:absolute;top:52px;width:100%;text-align:center;font-size:35px}
.approach .rule{position:absolute;left:577px;top:103px;width:46px;height:2px;background:var(--ink)}
.card{position:absolute;width:449px;height:173px;background:var(--white);box-shadow:0 1px 4px rgba(0,0,0,.08)}
.card.dark{background:var(--dark)}
.card svg{position:absolute;left:34px;top:30px}
.card h3{position:absolute;left:134px;top:42px;font-size:18px;font-weight:500;color:var(--ink)}
.card p{position:absolute;left:134px;top:72px;width:280px;font-size:12.5px;line-height:21px;color:#6b6e73}
.card.dark h3{color:var(--white)}
.card.dark p{color:#d8d9db}
.approach .outline-btn{left:512px;top:545px;width:180px;border-color:#4a4e55}

/* portfolio */
.portfolio{position:absolute;left:0;top:2013px;width:1200px;height:462px;background:var(--slate)}
.portfolio .section-title{position:absolute;left:158px;top:76px;color:var(--white);font-size:42px}
.portfolio .rule{position:absolute;left:160px;top:134px;width:57px;height:3px;background:var(--white)}
.portfolio .intro{position:absolute;left:517px;top:76px;width:560px;font-size:15.5px;line-height:28px;color:#b9bbbe}
.slide{position:absolute;overflow:hidden;z-index:2}
.slide .caption{position:absolute;left:18px;bottom:12px;color:var(--white)}
.slide .caption strong{display:block;font-size:19px;font-weight:700;line-height:24px}
.slide .caption span{display:inline-block;font-size:11px;font-weight:700;margin-top:4px;border-bottom:1px solid var(--white)}
.slide-left{left:160px;top:2240px;width:303px;height:305px;background:linear-gradient(180deg,#9ea1a4,#5f6368 55%,#33373c)}
.slide-center{left:463px;top:2208px;width:323px;height:367px;z-index:3;background:linear-gradient(160deg,#6fa6e0 0%,#8c6a50 45%,#3b3f46 75%,#1f2e48 100%);box-shadow:0 0 18px rgba(0,0,0,.35)}
.slide-center .caption{left:46px;bottom:24px}
.slide-right{left:786px;top:2247px;width:292px;height:308px;background:linear-gradient(200deg,#d8d9da,#8b8e92 50%,#2f3338)}
.slider-arrow{position:absolute;z-index:2}

/* team */
.team{position:absolute;left:0;top:2475px;width:1200px;height:690px;background:linear-gradient(90deg,#ffffff 0%,#f6f6f7 40%,#eef0f3 100%)}
.team-photo{position:absolute;left:560px;top:100px;width:640px;height:590px;background:linear-gradient(110deg,rgba(238,240,243,0) 0%,#c9ccd2 25%,#8d939c 55%,#e9c8b6 80%,#f3e3da 100%)}
.team .eyebrow{position:absolute;left:140px;top:234px}
.team .section-title{position:absolute;left:140px;top:260px;font-size:40px}
.team .rule{position:absolute;left:140px;top:320px;width:57px;height:3px;background:var(--ink)}
.team .body-text{position:absolute;left:140px;top:344px;width:450px;font-size:15.5px}
.team .outline-btn{left:140px;top:478px}

/* contact */
.contact{position:absolute;left:0;top:3165px;width:1200px;height:457px;background:linear-gradient(180deg,#2e333b 0%,#454a52 50%,#5a5f66 100%)}
.contact .section-title{position:absolute;top:112px;width:100%;text-align:center;color:var(--white);font-size:40px}
.contact .rule{position:absolute;left:576px;top:170px;width:48px;height:3px;background:var(--white)}
.contact .intro{position:absolute;top:188px;width:100%;text-align:center;font-size:15.5px;line-height:29px;color:#c6c8cb}
.contact .outline-btn{left:516px;top:267px;width:180px;height:45px;border-color:var(--white);color:var(--white)}

/* footer */
.site-footer{position:absolute;left:0;top:3622px;width:1200px;height:241px;background:var(--white)}
.footer-brand{position:absolute;left:0;top:24px;width:100%;text-align:center}
.footer-brand .brand-mark{width:40px;height:40px;margin-bottom:6px}
.footer-brand .brand-name{font-size:16px}
.footer-nav{position:absolute;top:116px;width:100%;display:flex;justify-content:center;gap:37px}
.footer-nav a{font-size:12px;font-weight:600;letter-spacing:.6px;color:var(--ink);text-decoration:none}
.copyright{position:absolute;top:146px;width:100%;text-align:center;font-size:11px;color:#777a7f}
.social{position:absolute;top:174px;left:553px;display:flex;gap:8px}
.social span{width:28px;height:28px;border-radius:50%;background:#9a9ca0;display:block}
</style>
</head>
<body>
<div class="page">

  <header class="site-header">
    <div class="brand">
      <span class="brand-mark"></span>
      <div class="brand-name">NORTHVALE EQUITIES</div>
      <div class="brand-tag">REAL ESTATE</div>
    </div>
    <div class="call-btn">
      <svg width="16" height="16" viewBox="0 0 24 24" fill="none" stroke="#fff" stroke-width="2"><path d="M5 3h4l2 5-3 2a11 11 0 0 0 6 6l2-3 5 2v4a2 2 0 0 1-2 2A18 18 0 0 1 3 5a2 2 0 0 1 2-2z"/></svg>
      CALL US (+100) 555 0147
    </div>
    <nav class="main-nav">
      <a class="active">OUR COMPANY</a>
      <a>INVESTMENT APPRAOCH</a>
      <a>EXECUTIVE TEAM</a>
      <a>INVESTMENT PORTFOLIO</a>
      <a>CONTACT</a>
    </nav>
  </header>

  <section class="hero" role="img" aria-label="Snow-covered mountain peaks under a deep blue sky">
    <h1 class="hero-title">NORTHVALE EQUITIES</h1>
    <div class="hero-sub">REAL ESTATE INVESTMENT FIRM</div>
    <div class="hero-btn fill">LEARN MORE</div>
    <div class="hero-btn ghost">CONTACT US</div>
  </section>

  <section class="about">
    <div class="about-bg-photo" role="img" aria-label="Faded grey skyscrapers"></div>
    <div class="about-frame"></div>
    <div class="about-dots"></div>
    <div class="about-photo" role="img" aria-label="Glass office towers seen from below with sunlight between them"></div>
    <div class="eyebrow">WHO WE ARE</div>
    <h2 class="section-title">ABOUT COMPANY</h2>
    <div class="rule"></div>
    <p class="body-text">Lorem ipsum dolor sit amet, consectetur adipiscing elit, sed do eiusmod tempor incididunt ut labore et dolore magna aliqua. Ut enim ad minim veniam, quis Dolore magna aliqua. Ut enim ad minim veniam, quis nostrud</p>
    <div class="outline-btn">LEARN MORE</div>
  </section>

  <section class="approach">
    <h2 class="section-title">INVESTMENT APPROACH</h2>
    <div class="rule"></div>

    <div class="card dark" style="left:150px;top:145px">
      <svg width="62" height="62" viewBox="0 0 62 62" fill="none" stroke="#fff" stroke-width="2"><circle cx="31" cy="16" r="12"/><path d="M31 9v14M35 12h-6a2 2 0 0 0 0 4h4a2 2 0 0 1 0 4h-6"/><path d="M4 38h8v16H4zM58 38h-8v16h8zM12 42l10-4 10 5 8-3 10 2M12 50h10l10 3 18-7"/></svg>
      <h3>ACQUISITIONS</h3>
      <p>Lorem ipsum dolor sit amet, consectetur adipiscing elit, sed do eiusmod tempor incididunt ut labore et dolore</p>
    </div>

    <div class="card" style="left:623px;top:145px">
      <svg width="62" height="62" viewBox="0 0 62 62" fill="none" stroke="#4a4e55" stroke-width="2"><circle cx="48" cy="10" r="7"/><path d="M8 56h46M10 56V44h6v12M22 56V38h6v18M34 56V32h6v24M46 56V26h6v30M10 36l14-8 10 4 12-12"/></svg>
      <h3>FINANCING</h3>
      <p>Lorem ipsum dolor sit amet, consectetur adipiscing elit, sed do eiusmod tempor incididunt ut labore et dolore</p>
    </div>

    <div class="card" style="left:150px;top:340px">
      <svg width="62" height="62" viewBox="0 0 62 62" fill="none" stroke="#4a4e55" stroke-width="2"><circle cx="24" cy="26" r="16"/><path d="M18 26l5 5 9-10"/><circle cx="42" cy="34" r="6"/><path d="M32 58v-8a10 10 0 0 1 20 0v8"/></svg>
      <h3>DUE DILIGENCE</h3>
      <p>Lorem ipsum dolor sit amet, consectetur adipiscing elit, sed do eiusmod tempor incididunt ut labore et dolore</p>
    </div>

    <div class="card" style="left:623px;top:340px">
      <svg width="62" height="62" viewBox="0 0 62 62" fill="none" stroke="#4a4e55" stroke-width="2"><circle cx="34" cy="22" r="14" stroke-dasharray="5 3"/><circle cx="34" cy="22" r="6"/><circle cx="14" cy="34" r="5"/><path d="M8 58v-6a6 6 0 0 1 12 0v6M24 40l6 6"/></svg>
      <h3>MANAGEMENT</h3>
      <p>Lorem ipsum dolor sit amet, consectetur adipiscing elit, sed do eiusmod tempor incididunt ut labore et dolore</p>
    </div>

    <div class="outline-btn">LEARN MORE</div>
  </section>

  <section class="portfolio">
    <h2 class="section-title">OUR PORTFOLIO</h2>
    <div class="rule"></div>
    <p class="intro">Lorem ipsum dolor sit amet, consectetur adipiscing elit, sed do eiusmod tempor incididunt ut labore et dolore magna aliqua.</p>
  </section>

  <section class="team">
    <div class="team-photo" role="img" aria-label="Two colleagues working together at a laptop in a bright office"></div>
    <div class="eyebrow">WHO WE ARE</div>
    <h2 class="section-title">MEET THE TEAM</h2>
    <div class="rule"></div>
    <p class="body-text">Lorem ipsum dolor sit amet, consectetur adipiscing elit, sed do eiusmod tempor incididunt ut labore et dolore magna aliqua. Ut enim ad minim veniam, quis Dolore magna aliqua. Ut enim ad minim venia.</p>
    <div class="outline-btn">LEARN MORE</div>
  </section>

  <div class="slide slide-left" role="img" aria-label="Black and white modern glass office building">
    <div class="caption"><strong>YOUR PROJECT HERE</strong><span>VIEW MORE</span></div>
  </div>
  <div class="slide slide-right" role="img" aria-label="Black and white angular building facade">
    <div class="caption"><strong>YOUR PROJECT HERE</strong><span>VIEW MORE</span></div>
  </div>
  <div class="slide slide-center" role="img" aria-label="Modern apartment building with blue balconies against the sky">
    <div class="caption"><strong>YOUR PROJECT HERE</strong><span>VIEW MORE</span></div>
  </div>
  <svg class="slider-arrow" style="left:102px;top:2384px" width="34" height="20" viewBox="0 0 34 20" fill="none" stroke="#c4c6c9" stroke-width="2"><path d="M33 10H2M10 2L2 10l8 8"/></svg>
  <svg class="slider-arrow" style="left:1102px;top:2400px" width="34" height="20" viewBox="0 0 34 20" fill="none" stroke="#ffffff" stroke-width="2"><path d="M1 10h31M24 2l8 8-8 8"/></svg>

  <section class="contact" role="img" aria-label="Dark tinted aerial view of a city skyline">
    <h2 class="section-title">GET IN TOUCH</h2>
    <div class="rule"></div>
    <p class="intro">Lorem ipsum dolor sit amet, consectetur adipiscing elit, sed do eiusmod<br>tempor incididunt ut labore et dolore magna aliqua.</p>
    <div class="outline-btn">CONTACT US</div>
  </section>

  <footer class="site-footer">
    <div class="footer-brand">
      <span class="brand-mark"></span>
      <div class="brand-name">NORTHVALE EQUITIES</div>
    </div>
    <nav class="footer-nav">
      <a>OUR COMPANY</a>
      <a>INVESTMENT APPRAOCH</a>
      <a>EXECUTIVE TEAM</a>
      <a>INVESTMENT PORTFOLIO</a>
      <a>CONTACT</a>
    </nav>
    <div class="copyright">© 2021 Northvale Equities | All Rights Reserved</div>
    <div class="social"><span></span><span></span><span></span></div>
  </footer>

</div>
</body>
</html>
```